Personalised Poetry business needs a business card designed

I am a writer that specialises in personalised poetry for people for significant life events.
I want a business card that stands out and portrays class and professionalism but is also welcoming & indicates warmth and honesty.
I'm happy with the logo that was designed for me, I would like to see it in raised print on the business card. I am open to suggestions on colours but think perhaps gold or silver writing for the logo would look good. I would like just the logo and my name and contact details on the front of the card. On the back of the card, I would like a list of the different events I provide poems for I will upload a photo of my current business card for reference. My current logo has a shading behind it that I don't like, I just want the words of the logo without any background colour

Target Market(s)

People wanting to provide a unique gift to someone special in their life

Industry/Entity Type

Writer

Contact Information for Business Card

Logo, my name and contact details on the front and a list of all the events I write poetry for on the back

Font styles to use
Script

Requirements
Must have
• I would like to see the logo, if possible, in a raised type of print on the card so that you can feel the actual words. I would like to have a glossy finish to the card and be able to print it on good quality board
Should not have
• The shading that is currently behind the logo on my current business card

```html
<!DOCTYPE html>
<html lang="en">
<head>
<meta charset="utf-8">
<title>Lines for Always – Business Card</title>
<link href="https://fonts.googleapis.com/css2?family=EB+Garamond:wght@400;500&family=Pinyon+Script&family=Questrial&display=swap" rel="stylesheet">
<style>
  :root {
    --backdrop: #ababab;
    --card: #f4f4f2;
    --gold: #a8784a;
    --gold-light: #c9a27a;
    --taupe: #8e7666;
    --heading: #9b8273;
  }
  html, body {
    margin: 0;
    width: 1200px;
    height: 1000px;
    overflow: hidden;
    background: var(--backdrop);
  }
  .canvas { position: relative; width: 1200px; height: 1000px; }
  .card {
    position: absolute;
    left: 293px;
    width: 614px;
    height: 354px;
    background: var(--card);
    box-shadow: 0 2px 5px rgba(0,0,0,0.35);
  }
  .card--front { top: 132px; }
  .card--back { top: 530px; }

  .brand-name {
    position: absolute;
    left: 70px; top: 100px;
    width: 420px;
    text-align: center;
    margin: 0;
    font-family: "EB Garamond", serif;
    font-weight: 400;
    font-size: 52px;
    line-height: 1;
    color: var(--gold);
  }
  .brand-tagline {
    position: absolute;
    left: 70px; top: 182px;
    width: 420px;
    text-align: center;
    margin: 0;
    font-family: "Questrial", sans-serif;
    font-size: 21px;
    color: var(--gold);
  }
  .divider-mark {
    position: absolute;
    left: 259px; top: 220px;
    width: 24px; height: 9px;
    border-radius: 5px;
    background: var(--gold-light);
  }
  .illustration-pen {
    position: absolute;
    left: 458px; top: 100px;
    width: 90px; height: 145px;
    border-radius: 0 45px 10px 30px;
    background: linear-gradient(160deg, rgba(201,162,122,0.3), rgba(168,120,74,0.5));
  }
  .contact-name {
    position: absolute;
    left: 0; top: 242px;
    width: 614px;
    text-align: center;
    margin: 0;
    font-family: "Pinyon Script", cursive;
    font-size: 31px;
    color: var(--gold);
  }
  .contact-line {
    position: absolute;
    left: 0;
    width: 614px;
    text-align: center;
    margin: 0;
    font-family: "EB Garamond", serif;
    font-size: 18px;
    color: var(--gold);
  }
  .contact-phone { top: 287px; }
  .contact-email { top: 310px; }

  .services-heading {
    position: absolute;
    left: 0; top: 42px;
    width: 614px;
    text-align: center;
    margin: 0;
    font-family: "Pinyon Script", cursive;
    font-weight: 400;
    font-size: 34px;
    color: var(--heading);
  }
  .services-list {
    position: absolute;
    top: 126px;
    margin: 0; padding: 0;
    list-style: none;
    font-family: "EB Garamond", serif;
    font-size: 25.5px;
    line-height: 48px;
    color: var(--taupe);
  }
  .services-list--left { left: 32px; }
  .services-list--right { left: 331px; }
</style>
</head>
<body>
<main class="canvas">
  <section class="card card--front">
    <div class="illustration-pen" role="img" aria-label="Line drawing of a hand holding a fountain pen with a flowing ink swirl"></div>
    <h1 class="brand-name">Lines for Always</h1>
    <p class="brand-tagline">Personalised Poetry</p>
    <div class="divider-mark" role="img" aria-label="Small infinity ornament"></div>
    <p class="contact-name">Miles Carrow</p>
    <p class="contact-line contact-phone">0400 123 456</p>
    <p class="contact-line contact-email">miles@linesforalways.com</p>
  </section>

  <section class="card card--back">
    <h2 class="services-heading">Momentous Life Events Personalise in Poetry</h2>
    <ul class="services-list services-list--left">
      <li>• Weddings &amp; Anniversaries</li>
      <li>• Birthdays &amp; Christmas</li>
      <li>• Valentines Day</li>
    </ul>
    <ul class="services-list services-list--right">
      <li>• Retirements, Business</li>
      <li>&amp; Corporate Events</li>
      <li>• Funerals &amp; Eulogies</li>
    </ul>
  </section>
</main>
</body>
</html>
```